依頼詳細
【ターゲット】
<今後>
30~40代 女性
会社員 主婦

◆サイトマップ
1.TOP
∟2.Concept
∟3.Staff(一覧)
∟4.Staff(詳細)
∟5.Menu
∟6.Shampoo/Treatment/Head spa
∟7.organic menu
∟8.Salon Gallery
∟9.News(一覧)
∟10.News(詳細)
∟11.Blog(一覧)
∟12.Blog(詳細)
∟13.Salon info
∟14.Recruit(求職者の皆様へ)
∟15.スタイリスト、アシスタント、理容師求人情報
∟16.アイリスト、ネイリスト求人情報
∟17.Q&A
∟18.Voice
∟19.Coupon
∟20.Contact
※TOPページへ、フローティングでついてくる予約アイコンを設けて頂きたいです。
※インスタも埋め込みをしたいので、そのスペースを設けて頂けると幸いです。

◆上記サイトマップについて
・グローバルメニューは
Concept、Staff、Menu、Blog、Salon info、Recruit、Contact
上記の項目を必須で組み込んでください。

◆参考にしたいサイト
http://temuro518.com/(このサイトの雰囲気にもうちょっとナチュラル感をプラスしたいです。)
http://www.salon-kuvela.jp/(このサイトくらいのフェミニン感が欲しいです。)
http://www.dompaseti.com/voice(フローティングでついてくる予約アイコンの参考)

◆現行サイト
http://tresmode-pk.com/

◆ミナトノート
https://beauty.minatonote.jp/slnH000472815/

※ワークブリッジの規約にもありますが、通常業務に支障が出る為
直接電話等のお問い合わせをお控え頂けますよう、ご協力の程お願い致します。
ご不明点等ありましたら、ワークブリッジ内メッセージで頂戴できますと幸いです。
シンプル 複雑
単色 カラフル
暗い 明るい
日常 高級
遊び心 厳粛
未来的 伝統的
女性的 男性的
茶系、グレー系、現在のHPへ使用しているカラーをそのまま引き継ぐ形でデザインをお願いいたします。
【素材について】

◆サロンの写真をダウンロードできるURLを下記に記載いたしますので、
ダウンロードしてご使用ください。
【ダウンロードURL:https://15.filevessel.nu/1201-q83ab2917c06dfe2874093815b27461d3

◆今回、ピクセルノ「https://jp.pixelno.com/」というサイトにて
制作中の間定期契約を致しました。デザインの際には、一度仮素材にて配置を頂き、ピクセルノ以外の素材は無料の物をご使用頂きたいです。
画像に番号が割り振られていますので、その番号をお教え頂ければ
こちらで正規データをダウンロード致します。
(画像の利用はマンスリーパック内でお願いいたします。)
お世話になっております。
提案数が芳しくないため、
期間を延長させて頂きます。
どうぞ自由な発想でご提案ください。
お世話になっております。
この度はご提案を頂きましてありがとうございます。

デザインの選定に時間がかかっておりますので、
選定期限を12月22日までに延長させて頂きます。

宜しくお願いいたします。

サロンの雰囲気に合っているため

この度はご提案を頂きありがとうございます。
またの機会がありましたら、よろしくおねがいいたします。

```html
<!DOCTYPE html>
<html lang="ja">
<head>
<meta charset="utf-8">
<title>hair atelier TM</title>
<link rel="stylesheet" href="https://fonts.googleapis.com/css2?family=Cormorant+Garamond:wght@400;500;600&family=Noto+Serif+JP:wght@300;400;500&display=swap">
<style>
:root{
  --bg:#ffffff;
  --ink:#4a433e;
  --ink-soft:#857a72;
  --line:#cfcac5;
  --brown:#5e5048;
  --brown-dark:#3f3630;
  --wood:#b59c82;
  --stone:#d9d3cc;
  --hair:#7d6452;
  --green:#7fa35a;
}
*{box-sizing:border-box;margin:0;padding:0}
html,body{width:1200px;height:4848px;overflow:hidden;background:var(--bg)}
body{position:relative;font-family:"Noto Serif JP",serif;color:var(--ink);font-size:13px;line-height:1.7}
.abs{position:absolute}
.en{font-family:"Cormorant Garamond",serif}
.photo{position:absolute}
.frame{position:absolute;border:1px solid var(--line)}
.title{position:absolute}
.title h2{font-family:"Cormorant Garamond",serif;font-weight:500;font-size:38px;line-height:1;color:var(--ink)}
.title span{display:block;margin-top:10px;font-size:11px;color:var(--ink-soft);letter-spacing:.1em}
.title span::before{content:"";display:inline-block;width:40px;height:1px;background:var(--ink-soft);vertical-align:middle;margin-right:10px}
.btn{position:absolute;background:var(--brown);color:#fff;font-size:12px;text-align:center;line-height:30px;height:30px;letter-spacing:.1em}
.btn::after{content:" ›"}

/* header */
.logo{left:40px;top:18px;font-family:"Cormorant Garamond",serif;font-size:26px;font-weight:500;line-height:1;color:var(--ink)}
.gnav{left:420px;top:30px;display:flex;gap:24px;font-family:"Cormorant Garamond",serif;font-size:17px}
.tel{right:60px;top:8px;text-align:right}
.tel small{display:block;font-size:10px;color:var(--ink-soft)}
.tel b{font-family:"Cormorant Garamond",serif;font-size:22px;font-weight:500}
.hero{left:60px;top:58px;width:940px;height:580px;background:linear-gradient(160deg,#efe9e2 0%,#cfc3b4 45%,#a99680 75%,#d6cbbd 100%)}
.reserve{left:40px;top:520px;width:140px;height:140px;border-radius:50%;background:#fff;border:2px solid var(--green);display:flex;flex-direction:column;align-items:center;justify-content:center;font-size:15px;color:var(--ink);line-height:1.4;text-align:center}
.reserve small{font-family:"Cormorant Garamond",serif;font-size:12px;color:var(--ink-soft)}
.dots{left:560px;top:660px;display:flex;gap:8px}
.dots i{width:8px;height:8px;border-radius:50%;border:1px solid var(--line);display:block}
.dots i:first-child{background:var(--ink-soft)}

/* concept */
.concept-copy{left:760px;top:725px;height:280px;writing-mode:vertical-rl;font-size:15px;line-height:2.1;letter-spacing:.12em}
.concept-copy p + p{margin-right:20px}
.concept-copy strong{font-size:19px;font-weight:500}

/* staff */
.staff-name{writing-mode:vertical-rl;font-size:22px;letter-spacing:.3em}
.staff-role{writing-mode:vertical-rl;font-size:10px;color:var(--ink-soft);line-height:1.6}
.staff-box{border:1px solid var(--line);border-radius:8px;padding:14px 18px 50px;font-size:11px;line-height:1.8;color:var(--ink-soft)}

/* menu */
.price{width:290px;font-size:13px}
.price li{list-style:none;display:flex;justify-content:space-between;line-height:28px}
.sub{font-family:"Cormorant Garamond",serif;font-size:20px;color:var(--ink)}

/* blog */
.blog-list li{list-style:none;display:flex;gap:30px;line-height:26px;font-size:12px}
.blog-list time{font-family:"Cormorant Garamond",serif;font-size:15px;color:var(--ink-soft)}
.insta{left:472px;top:2860px;display:grid;grid-template-columns:repeat(4,128px);grid-template-rows:repeat(3,96px);gap:6px}
.insta div{background:linear-gradient(135deg,#d8cfc4,#9c8877)}

/* salon info */
.info-logo{left:700px;top:3420px;display:flex;align-items:center;gap:14px;font-family:"Cormorant Garamond",serif;font-size:26px}
.info-logo i{width:56px;height:56px;border:1px solid var(--ink-soft);border-radius:50%;display:block}
.info-table{left:630px;top:3510px;width:350px;border-collapse:collapse;font-size:11px}
.info-table th{text-align:left;font-weight:500;width:90px;padding:10px 0;vertical-align:top;border-bottom:1px solid var(--line)}
.info-table td{padding:10px 0;border-bottom:1px solid var(--line);color:var(--ink-soft)}

/* footer */
.footer{left:60px;top:4430px;width:1080px;height:418px;background:linear-gradient(180deg,#c9c1b8,#a39789 60%,#8b7e72)}
.footer-mark{left:565px;top:4412px;width:70px;height:70px;border-radius:50%;background:var(--brown);color:#fff;font-family:"Cormorant Garamond",serif;font-size:16px;display:flex;align-items:center;justify-content:center}
.fcol{color:#fff;font-size:12px;line-height:22px}
.fcol h3{font-family:"Cormorant Garamond",serif;font-weight:500;font-size:18px;margin-bottom:6px}
.fcol li{list-style:none}
.fcol li::before{content:"- "}
.coupon{left:430px;top:4700px;width:340px;height:58px;background:var(--brown-dark);color:#fff;display:flex;align-items:center;justify-content:center;gap:12px;font-size:15px}
.coupon b{font-family:"Cormorant Garamond",serif;font-size:34px;font-weight:500}
.sns{top:4716px;width:26px;height:26px;background:#fff}
.copy{left:0;top:4815px;width:1200px;text-align:center;font-size:10px;color:#fff}
</style>
</head>
<body>

<!-- header -->
<div class="abs logo">hair atelier TM</div>
<nav class="abs gnav"><span>Concept</span><span>Staff</span><span>Menu</span><span>Blog</span><span>Salon info</span><span>Recruit</span><span>Contact</span></nav>
<div class="abs tel"><small>予約・お問い合わせ</small><b>03-4418-2907</b></div>
<div class="photo hero" role="img" aria-label="明るい木目の床と鏡台が並ぶサロン店内"></div>
<div class="abs reserve"><small>Reserve</small>Web予約は<br>コチラ</div>
<div class="abs dots"><i></i><i></i><i></i><i></i><i></i><i></i></div>

<!-- concept -->
<div class="frame" style="left:310px;top:700px;width:690px;height:180px;border-bottom:none;border-left:none"></div>
<div class="frame" style="left:310px;top:700px;width:1px;height:180px;border-width:0 0 0 1px"></div>
<div class="title" style="left:350px;top:760px"><h2>Concept</h2><span>コンセプト</span></div>
<div class="abs concept-copy">
  <p><strong>「素敵な自分に」</strong></p>
  <p>百年後も行きたい場所がある</p>
  <p>仕事をする美容室に。</p>
  <p>大人の女性が自然体で</p>
  <p>通い続けられる空間を、</p>
  <p>丁寧な技術と心でお届けします。</p>
</div>
<div class="photo" style="left:280px;top:880px;width:280px;height:240px;background:linear-gradient(150deg,#6d5a4c,#3a302a 60%,#8a7867)" role="img" aria-label="窓辺のテーブルと小物の写真"></div>

<!-- staff -->
<div class="frame" style="left:560px;top:1180px;width:440px;height:470px;border-left:none;border-bottom:none"></div>
<div class="title" style="left:930px;top:1230px"><h2 style="font-size:30px">Staff</h2><span>スタッフ</span></div>
<div class="photo" style="left:560px;top:1230px;width:180px;height:140px;background:linear-gradient(160deg,#dfe3e6,#5b6673)" role="img" aria-label="スタッフのポートレート写真"></div>
<div class="abs staff-name" style="left:755px;top:1230px">森本 健司</div>
<div class="abs staff-role" style="left:850px;top:1300px">代表<br>Kenji Morimoto</div>
<div class="abs staff-box" style="left:200px;top:1250px;width:340px;height:120px">お客様の髪質とライフスタイルに合わせた再現性の高いスタイルをご提案いたします。お気軽にご相談ください。</div>
<div class="btn" style="left:390px;top:1330px;width:120px">詳細を見る</div>
<div class="photo" style="left:560px;top:1490px;width:180px;height:150px;background:linear-gradient(160deg,#e9e9e9,#6d6a68)" role="img" aria-label="スタッフのポートレート写真"></div>
<div class="abs staff-name" style="left:755px;top:1420px">高野 亮太</div>
<div class="abs staff-role" style="left:850px;top:1460px">スタイリスト<br>Ryota Takano</div>
<div class="abs staff-box" style="left:200px;top:1480px;width:340px;height:120px">やわらかな質感のカラーとカットが得意です。毎日のお手入れが楽になる髪型を一緒に見つけましょう。</div>
<div class="btn" style="left:390px;top:1560px;width:120px">詳細を見る</div>

<!-- menu -->
<div class="frame" style="left:200px;top:1820px;width:360px;height:740px;border-right:none;border-bottom:none"></div>
<div class="title" style="left:300px;top:1860px"><h2 style="font-size:30px">Menu</h2><span>メニュー</span></div>
<ul class="abs price" style="left:220px;top:1950px">
  <li><span>カット</span><span>¥6,800</span></li>
  <li><span>カラー</span><span>¥6,500〜</span></li>
  <li><span>パーマ</span><span>¥8,500〜</span></li>
  <li><span>シャンプー＆ブロー</span><span>¥3,500</span></li>
  <li><span>トリートメント</span><span>¥2,000</span></li>
  <li><span>ヘッドスパ</span><span>¥2,500</span></li>
  <li><span>ヘアーセット</span><span>¥4,000</span></li>
</ul>
<div class="btn" style="left:220px;top:2190px;width:110px">more</div>
<div class="title" style="left:300px;top:2270px"><span style="margin-top:0">スパ</span></div>
<ul class="abs price" style="left:220px;top:2330px">
  <li><span>ヘッドスパコース</span><span>¥5,000</span></li>
  <li><span>ケアカラー</span><span>¥7,500</span></li>
  <li><span>フルケアコース</span><span>¥8,000</span></li>
  <li><span>スペシャルコース</span><span>¥10,000</span></li>
</ul>
<div class="btn" style="left:220px;top:2490px;width:110px">more</div>
<div class="photo" style="left:560px;top:1860px;width:440px;height:420px;background:linear-gradient(135deg,#f2f0ee,#a8917e 55%,#6b5444)" role="img" aria-label="ボブスタイルのヘアモデル写真"></div>
<div class="photo" style="left:560px;top:2290px;width:216px;height:240px;background:linear-gradient(135deg,#d7c4b4,#8a6550)" role="img" aria-label="ロングヘアのモデル写真"></div>
<div class="photo" style="left:784px;top:2290px;width:216px;height:240px;background:linear-gradient(135deg,#f0efed,#4e4440)" role="img" aria-label="ショートヘアのモデル写真"></div>

<!-- blog -->
<div class="frame" style="left:200px;top:2600px;width:800px;height:200px;border-bottom:none;border-right:none"></div>
<div class="title" style="left:260px;top:2620px"><h2 style="font-size:30px">Blog</h2><span>ブログ</span></div>
<ul class="abs blog-list" style="left:420px;top:2625px">
  <li><time>2018.12.01</time><span>新しいヘアカラーのご案内です。</span></li>
  <li><time>2018.12.01</time><span>冬のお手入れについてのお話。</span></li>
  <li><time>2018.12.01</time><span>年末年始の営業日のお知らせ。</span></li>
  <li><time>2018.12.01</time><span>スタッフおすすめのケア用品。</span></li>
</ul>
<div class="btn" style="left:880px;top:2755px;width:110px">more</div>

<!-- instagram -->
<div class="title" style="left:260px;top:2860px"><h2 style="font-size:30px">Instagram</h2><span>インスタ</span></div>
<div class="abs insta" role="img" aria-label="インスタグラム投稿の写真一覧">
  <div></div><div style="background:linear-gradient(135deg,#e8e2c8,#a9a06a)"></div><div style="background:linear-gradient(135deg,#c9b8a3,#6d5a48)"></div><div style="background:linear-gradient(135deg,#d9c27a,#7a5a8a)"></div>
  <div style="background:linear-gradient(135deg,#ece8e2,#8b8079)"></div><div style="background:linear-gradient(135deg,#b38b6c,#4a3428)"></div><div style="background:linear-gradient(135deg,#7a6a5e,#2f2a27)"></div><div style="background:linear-gradient(135deg,#c7b09a,#5f4a3c)"></div>
  <div style="background:linear-gradient(135deg,#a58f7a,#3d332d)"></div><div style="background:linear-gradient(135deg,#e3dbd2,#9b8b7d)"></div><div style="background:linear-gradient(135deg,#bfa48a,#6b5040)"></div><div style="background:linear-gradient(135deg,#d6c3a8,#866a52)"></div>
</div>

<!-- salon info -->
<div class="frame" style="left:200px;top:3200px;width:800px;height:700px;border-bottom:none"></div>
<div class="title" style="left:520px;top:3250px;text-align:center"><h2 style="font-size:32px">Salon info</h2><span>サロン情報</span></div>
<div class="photo" style="left:200px;top:3400px;width:360px;height:450px;background:linear-gradient(170deg,#6b5444,#c2ae98 45%,#e8e2da)" role="img" aria-label="梁のある天井と窓辺のサロン内観写真"></div>
<div class="abs info-logo"><i></i>hair atelier TM</div>
<table class="abs info-table">
  <tr><th>電話番号</th><td>03-4418-2907</td></tr>
  <tr><th>メールアドレス</th><td>info@tresmode-pk.com</td></tr>
  <tr><th>住所</th><td>〒150-0042<br>東京都渋谷区緑町2-14-3<br>緑町テラス1F</td></tr>
  <tr><th>交通アクセス</th><td>緑町駅より徒歩5分<br>桜坂駅より徒歩8分<br>駐車場はございません</td></tr>
  <tr><th>営業時間</th><td>平日 10:00〜20:00<br>土日祝 9:00〜19:00<br>定休日 火曜日</td></tr>
</table>

<!-- contact / recruit -->
<div class="frame" style="left:200px;top:3940px;width:360px;height:420px;border-right:none;border-bottom:none"></div>
<div class="title" style="left:300px;top:3985px;text-align:center"><h2 style="font-size:28px">Contact</h2><span>お問い合わせ</span></div>
<div class="photo" style="left:220px;top:4070px;width:320px;height:230px;background:linear-gradient(170deg,#dfe4e8,#f4f4f2 50%,#8c8a86)" role="img" aria-label="白い外壁のサロン外観写真"></div>
<div class="btn" style="left:380px;top:4310px;width:140px">詳細はこちら</div>
<div class="frame" style="left:640px;top:3940px;width:360px;height:420px;border-left:none;border-bottom:none"></div>
<div class="title" style="left:740px;top:3985px;text-align:center"><h2 style="font-size:28px">Recruit</h2><span>スタッフ募集</span></div>
<div class="photo" style="left:660px;top:4070px;width:320px;height:230px;background:linear-gradient(150deg,#e0cdb8,#9b6e50 55%,#5a4034)" role="img" aria-label="髪を仕上げる施術風景の写真"></div>
<div class="btn" style="left:820px;top:4310px;width:140px">詳細はこちら</div>

<!-- footer -->
<div class="photo footer" role="img" aria-label="サロン店内をぼかした背景写真"></div>
<div class="abs footer-mark">TM</div>
<div class="abs fcol" style="left:260px;top:4520px"><h3>hair atelier TM</h3><ul><li>Concept</li><li>Staff</li><li>Menu</li><li>Blog</li><li>Salon info</li><li>Q&amp;A</li><li>Voice</li><li>Coupon</li><li>Contact</li></ul></div>
<div class="abs fcol" style="left:500px;top:4520px"><h3>Menu</h3><ul><li>Shampoo</li><li>Treatment</li><li>Head spa</li><li>Organic menu</li><li>Salon Gallery</li></ul></div>
<div class="abs fcol" style="left:740px;top:4520px"><h3>Recruit</h3><ul><li>求職者の皆様へ</li><li>スタイリスト求人</li><li>アイリスト求人</li></ul></div>
<div class="abs coupon"><span>初回限定</span><b>20%</b><span>OFF</span></div>
<div class="abs sns" style="left:880px"></div>
<div class="abs sns" style="left:914px"></div>
<div class="abs copy">Copyright © hair atelier TM All Rights Reserved.</div>

</body>
</html>
```